Business card - mobile service

O KiraTel is a mobile family safety service based on tablets and smartphones.
The business card must have:
BASIC INFO
Company Logo
Name
Position / Job Title: Co-founder
Mobile Phone Number: +55 (11) 5080 6172
Land Line: +55 (11) 9087 614352
Email Address: name@kiratel-example.com
Web Site URL: www.kiratel-example.com
PROMOTIONAL INFO
Try KiraTel free Today!
Your personal promo code: xxxx-2222-uuuu-7777-1234
Promo code text explanation with the instructions about the trial offer
Updates
Dears,
One more must have: the KiraTel slogan:
Industry/Entity Type
Safety
Look and feel
Each slider illustrates characteristics of the customer's brand and the style your logo design should communicate.

```html
<!DOCTYPE html>
<html lang="en">
<head>
<meta charset="utf-8">
<title>KiraTel business card</title>
<link rel="stylesheet" href="https://fonts.googleapis.com/css2?family=Open+Sans:wght@400;600;700;800&display=swap">
<style>
  :root {
    --brand-blue: #00a0e0;
    --brand-yellow: #fdc614;
    --ink: #231f20;
    --paper: #ffffff;
    --backdrop: #ffffff;
    --shadow: rgba(0, 0, 0, 0.22);
  }
  * { margin: 0; padding: 0; box-sizing: border-box; }
  html, body {
    width: 1200px; height: 900px; overflow: hidden;
    background: var(--backdrop);
    font-family: "Open Sans", sans-serif;
  }
  .stage { position: relative; width: 1200px; height: 900px; }

  .card { position: absolute; box-shadow: 4px 6px 10px var(--shadow); }

  .card-back {
    left: 468px; top: 420px; width: 648px; height: 395px;
    background: var(--brand-blue);
    border-radius: 38px;
    color: var(--paper);
  }
  .card-front {
    left: 85px; top: 85px; width: 647px; height: 393px;
    background: var(--paper);
    border-radius: 0 40px 40px 40px;
    color: var(--ink);
    z-index: 2;
  }

  /* front */
  .wordmark {
    position: absolute; left: 32px; top: 52px;
    display: flex; align-items: center; gap: 14px;
  }
  .wordmark-name {
    font-weight: 800; font-size: 70px; line-height: 1;
    color: var(--brand-blue); letter-spacing: -1px;
    white-space: nowrap;
  }
  .wordmark-dot {
    flex: none;
    width: 26px; height: 26px; border-radius: 50%;
    background: var(--brand-yellow);
  }
  .slogan {
    position: absolute; left: 175px; top: 135px;
    font-size: 14px; color: var(--ink);
  }
  .contact { position: absolute; left: 355px; top: 172px; }
  .person-name { font-size: 23px; font-weight: 700; line-height: 32px; }
  .person-role { font-size: 16px; line-height: 24px; }
  .phones { margin-top: 16px; font-size: 16px; line-height: 24px; }
  .phones dt { font-weight: 700; float: left; clear: left; width: 86px; }
  .phones dd { margin-left: 86px; }
  .web { margin-top: 22px; font-size: 16px; line-height: 24px; }
  .web b { display: inline-block; width: 18px; font-weight: 700; text-align: center; margin-right: 2px; }

  /* back */
  .wordmark-large {
    position: absolute; left: 34px; top: 155px;
    display: flex; align-items: center; gap: 12px;
  }
  .wordmark-large .wordmark-name {
    color: var(--paper); font-size: 60px; letter-spacing: -1px;
  }
  .wordmark-large .wordmark-dot { width: 28px; height: 28px; }
  .promo {
    position: absolute; left: 321px; top: 118px;
    font-size: 16.5px; line-height: 23px; font-weight: 400;
  }
  .promo p + p { margin-top: 22px; }
</style>
</head>
<body>
<div class="stage">

  <section class="card card-back" aria-label="Card back">
    <div class="wordmark-large">
      <span class="wordmark-name">KiraTel</span>
      <span class="wordmark-dot"></span>
    </div>
    <div class="promo">
      <p>Try KiraTel free Today!</p>
      <p>Your personal promo code<br>xxxx-2222-uuuu-7777-1234</p>
      <p>Promo code text explanation with<br>the instructions about the trial offer</p>
    </div>
  </section>

  <section class="card card-front" aria-label="Card front">
    <div class="wordmark">
      <span class="wordmark-name">KiraTel</span>
      <span class="wordmark-dot"></span>
    </div>
    <p class="slogan">Your Family Safety Service</p>
    <div class="contact">
      <h1 class="person-name">Marta Okoye</h1>
      <p class="person-role">Co-founder</p>
      <dl class="phones">
        <dt>Land Line</dt><dd>+55 (11) 9087 614352</dd>
        <dt>Mobile</dt><dd>+55 (11) 5080 6172</dd>
      </dl>
      <p class="web"><b>e</b>name@kiratel-example.com<br><b>w</b>www.kiratel-example.com</p>
    </div>
  </section>

</div>
</body>
</html>
```